Lotus Leaf Kitchen Road Billboard

Road Billboard I need all of this information on it
Authentic Thai Food Bangkok Style
6.5 Miles on the right
4126 Maple Ridge Rd Otto NC
828-555-4172

```html
<!DOCTYPE html>
<html lang="en">
<head>
<meta charset="utf-8">
<title>Lotus Leaf Kitchen – Road Billboard</title>
<link href="https://fonts.googleapis.com/css2?family=Kurale&family=Oswald:wght@500;600&family=Montserrat:wght@500&display=swap" rel="stylesheet">
<style>
  :root {
    --page: #cfcfcf;
    --mustard: #d8a727;
    --ink: #111111;
    --thai-red: #8e1a17;
    --white: #ffffff;
    --ember-dark: #140b06;
    --ember-mid: #7a2d0e;
    --ember-hot: #e0741f;
  }
  * { margin: 0; padding: 0; box-sizing: border-box; }
  html, body { width: 985px; height: 1200px; overflow: hidden; background: var(--page); }
  .billboard {
    position: absolute;
    left: 20px; top: 365px;
    width: 1285px; height: 640px;
    transform: scale(0.7354);
    transform-origin: top left;
    background: var(--mustard);
    overflow: hidden;
  }
  .billboard-art { position: absolute; inset: 0; width: 1285px; height: 640px; }
  .brand {
    position: absolute; left: 0; width: 555px; top: 128px;
    display: flex; justify-content: center; align-items: center; gap: 12px;
    font-family: "Kurale", serif; font-size: 30px; color: var(--ink);
  }
  .brand-dot { width: 16px; height: 16px; border-radius: 50%; background: var(--ink); }
  .headline {
    position: absolute; left: 0; width: 555px; top: 188px;
    text-align: center; font-family: "Kurale", serif; font-weight: 400; color: var(--ink);
    line-height: 1;
  }
  .headline-authentic { display: block; font-size: 56px; }
  .headline-thai { display: block; font-size: 98px; color: var(--thai-red); margin-top: -2px; letter-spacing: -1px; }
  .headline-style { display: block; font-size: 70px; margin-top: -8px; }
  .headline-rule {
    position: absolute; left: 230px; top: 420px; width: 92px; height: 4px; background: var(--thai-red);
  }
  .address {
    position: absolute; left: 48px; top: 460px;
    display: flex; align-items: center; gap: 14px;
    font-family: "Montserrat", sans-serif; font-weight: 500; font-size: 35px; color: var(--ink);
    white-space: nowrap;
  }
  .address-pin { width: 32px; height: 46px; }
  .phone {
    position: absolute; left: 44px; top: 508px;
    font-family: "Oswald", sans-serif; font-weight: 600; font-size: 100px; line-height: 1.1;
    color: var(--white); letter-spacing: -1px; white-space: nowrap;
  }
  .directions {
    position: absolute; left: 652px; top: 536px; width: 430px; height: 76px;
    display: flex; align-items: center; white-space: nowrap;
    font-family: "Oswald", sans-serif; font-weight: 500; font-size: 45px;
    color: var(--thai-red); letter-spacing: -0.5px;
  }
</style>
</head>
<body>
  <div class="billboard">
    <svg class="billboard-art" viewBox="0 0 1285 640">
      <defs>
        <radialGradient id="wok-fire" cx="0.5" cy="0.45" r="0.75">
          <stop offset="0" stop-color="#e0741f"/>
          <stop offset="0.45" stop-color="#7a2d0e"/>
          <stop offset="1" stop-color="#140b06"/>
        </radialGradient>
      </defs>
      <path class="food-photo" role="img" aria-label="Flaming wok stir-fry with shrimp, broccoli and vegetables"
            d="M525,0 H1285 V640 H900 Q640,430 525,0 Z" fill="url(#wok-fire)"/>
      <path class="swoosh-white" d="M540,180 Q640,430 830,560" fill="none" stroke="#ffffff" stroke-width="48"/>
      <path class="swoosh-black" d="M540,310 Q690,520 920,640" fill="none" stroke="#111111" stroke-width="44"/>
      <path class="direction-sign" d="M625,528 H1185 L1240,574 L1185,620 H625 Z" fill="#ffffff"/>
      <g class="direction-chevrons" fill="none" stroke-width="8">
        <path d="M1100,540 L1134,574 L1100,608" stroke="#111111"/>
        <path d="M1124,540 L1158,574 L1124,608" stroke="#8e1a17"/>
        <path d="M1148,540 L1182,574 L1148,608" stroke="#111111"/>
      </g>
    </svg>

    <div class="brand"><span class="brand-dot"></span>Lotus Leaf Kitchen</div>

    <h1 class="headline">
      <span class="headline-authentic">Authentic</span>
      <span class="headline-thai">Thai Food</span>
      <span class="headline-style">Bangkok Style</span>
    </h1>
    <div class="headline-rule"></div>

    <div class="address">
      <svg class="address-pin" viewBox="0 0 32 46">
        <path d="M16,0 C7,0 0,7 0,16 C0,28 16,46 16,46 C16,46 32,28 32,16 C32,7 25,0 16,0 Z M16,22 A7,7 0 1,1 16,8 A7,7 0 1,1 16,22 Z" fill="#8e1a17" fill-rule="evenodd"/>
      </svg>
      <span>4126 Maple Ridge Rd Otto NC</span>
    </div>

    <div class="phone">828-555-4172</div>

    <div class="directions">6.5 MILES ON THE RIGHT</div>
  </div>
</body>
</html>
```